Oil and Gas Letterhead Design Tweak

Simple letterhead information and design tweak.

Please note, we don't want to change the design or logo of the letterhead only the small changes mentioned below.

We need to change the company name up top to "Northvale Petrotek FZCO"

Also, we need to include in the footer the following information. I have attached an image of roughly how we would like to have it displayed in the footer.

Footer Details:

Northvale Petrotek FZCO,
Unit No. 2378, FZCO Trade Hub, level No. 1, K&P 7, Dubai, United Arab Emirates
Northvale Petrotek FZCO is registered as a free zone company under the rules & regulations of FZCO

Target Market(s)

O&G Market

Industry/Entity Type

Oil And Gas

Font styles to use
Sans Serif

Colors

Designer to choose colors to be used in the design.

Requirements
Must have
• Change the company name to Northvale Petrotek FZCO
• Include the footer on the bottom of the first and continuation page
Should not have
• Should not change the design or logo of the letterhead, only the specified changes mentioned above

```html
<!DOCTYPE html>
<html lang="en">
<head>
<meta charset="utf-8">
<title>Northvale Petrotek FZCO – Letterhead</title>
<link href="https://fonts.googleapis.com/css2?family=Lato:wght@400;700&family=Arimo:wght@700&display=swap" rel="stylesheet">
<style>
  :root {
    --backdrop: #e4e5e6;
    --paper: #ffffff;
    --brand-blue: #1a4fa3;
    --brand-red: #e31e2d;
    --ink: #2b2b2b;
    --ink-soft: #3c3c3c;
    --navy: #1d2a44;
    --sign-tone: #e9e9ec;
  }
  * { box-sizing: border-box; margin: 0; padding: 0; }
  html, body { width: 1200px; height: 1040px; overflow: hidden; }
  body {
    background: var(--backdrop);
    font-family: "Lato", sans-serif;
    color: var(--ink);
  }
  .letterhead {
    position: absolute;
    left: 254px;
    top: 30px;
    width: 693px;
    height: 980px;
    background: var(--paper);
    box-shadow: 0 2px 10px rgba(0,0,0,0.08);
  }
  .top-bands { position: absolute; left: 0; top: 0; width: 693px; height: 14px; }
  .brand {
    position: absolute;
    left: 150px;
    top: 58px;
    display: flex;
    align-items: center;
    gap: 12px;
  }
  .brand-mark { width: 18px; height: 18px; background: var(--brand-red); }
  .brand-name {
    font-family: "Lato", sans-serif;
    font-weight: 400;
    font-size: 21px;
    letter-spacing: 1.6px;
    text-transform: uppercase;
    color: var(--navy);
  }
  .letter-body {
    position: absolute;
    left: 96px;
    top: 190px;
    width: 500px;
  }
  .salutation {
    font-family: "Arimo", sans-serif;
    font-weight: 700;
    font-size: 15px;
    color: #111;
    margin-bottom: 14px;
  }
  .letter-body p.copy {
    font-size: 13.5px;
    line-height: 1.38;
    text-align: justify;
    color: var(--ink-soft);
    margin: 0 0 20px 18px;
  }
  .signature {
    display: block;
    margin: 26px 0 0 62px;
    width: 90px;
    height: 32px;
    background: var(--sign-tone);
    border-radius: 3px;
  }
  .footer {
    position: absolute;
    left: 200px;
    bottom: 58px;
    width: 470px;
  }
  .footer-name {
    font-size: 12.5px;
    font-weight: 700;
    letter-spacing: 0.6px;
    text-transform: uppercase;
    color: var(--navy);
  }
  .footer-line {
    font-size: 10.5px;
    line-height: 1.45;
    color: var(--ink);
  }
  .footer-rule {
    position: absolute;
    left: 0;
    bottom: -8px;
    width: 400px;
    height: 1.5px;
    background: var(--brand-red);
  }
  .footer-flags { position: absolute; right: 0; bottom: -8px; width: 70px; height: 12px; }
</style>
</head>
<body>
  <main class="letterhead">
    <svg class="top-bands" viewBox="0 0 693 14" aria-hidden="true">
      <polygon points="0,0 180,0 176,10 0,10" fill="var(--brand-blue)"/>
      <polygon points="238,0 693,0 693,8 234,11" fill="var(--brand-red)"/>
    </svg>

    <header class="brand">
      <span class="brand-mark"></span>
      <span class="brand-name">Northvale Petrotek FZCO</span>
    </header>

    <section class="letter-body">
      <p class="salutation">Dear Mr. Harlan,</p>
      <p class="copy">Lorem Ipsum is simply dummy text of the printing and typesetting industry. Lorem Ipsum has been the industry's standard dummy text ever since the 1500s, when an unknown printer took a galley of type and scrambled it to make a type specimen book. It has survived not only five centuries, but also the leap into electronic typesetting, remaining essentially unchanged.</p>
      <p class="copy">The standard chunk of Lorem Ipsum used since the 1500s is reproduced below for those interested. Sections 1.10.32 and 1.10.33 from "de Finibus Bonorum et Malorum" by Tullian are also reproduced in their exact original form, accompanied by English versions from the 1914 translation by H.Calloway</p>
      <p class="copy">Lorem Ipsum is simply dummy text of the printing and typesetting industry. Lorem Ipsum has been the industry's standard dummy text ever since the 1500s, when an unknown printer took a galley of type and scrambled it to make a type specimen book. It has survived not only five centuries, but also the leap into electronic typesetting, remaining essentially unchanged. It was popularised in the</p>
      <p class="copy">The standard chunk of Lorem Ipsum used since the 1500s is reproduced below for those interested. Sections 1.10.32 and 1.10.33 from "de Finibus Bonorum et Malorum" by Tullian are also reproduced in their exact original form, accompanied by English versions from the 1914 translation by H.Calloway</p>
      <span class="signature" role="img" aria-label="Handwritten signature of the sender"></span>
    </section>

    <footer class="footer">
      <p class="footer-name">Northvale Petrotek FZCO,</p>
      <p class="footer-line">Unit No. 2378, FZCO Trade Hub, level No. 1, K&amp;P 7, Dubai, United Arab Emirates</p>
      <p class="footer-line">Northvale Petrotek FZCO is registered as a free zone company under the rules &amp; regulations of FZCO</p>
      <span class="footer-rule"></span>
      <svg class="footer-flags" viewBox="0 0 70 12" aria-hidden="true">
        <polygon points="0,2 28,2 28,12 0,12" fill="var(--brand-blue)"/>
        <polygon points="36,2 62,0 70,6 36,12" fill="var(--brand-red)"/>
      </svg>
    </footer>
  </main>
</body>
</html>
```